Maple 3 Adjustable Pillow Package Design

I need a package design for our Maple 3 Adjustable Memory Foam Pillow. We offer comfort solutions that will help you live a pain-free, healthier & happier life. Our name Maple 3 means a state of bliss, elation or happiness. We will capitalize on the popularity of the term “On Maple 3” by selling the emotion of contented happiness that comes from owning our products. Our products improve the lives of our customers and we will market that by creating experiences that are memorable and keep people coming back. I have attached the template (print area) that must be followed.

Industry/Entity Type

Health & Wellness

Colors
0054AA
0677BA
7BADD7
CADEEF
E8F1F8

Requirements
Nice to have
• I have attached a few different examples.

```html
<!DOCTYPE html>
<html lang="en">
<head>
<meta charset="utf-8">
<title>Maple 3 Adjustable Pillow – Package Sleeve</title>
<link href="https://fonts.googleapis.com/css2?family=Cousine:wght@400;700&family=Montserrat:wght@500;600;700;800&display=swap" rel="stylesheet">
<style>
  :root {
    --band-light: #1fa2de;
    --band-dark: #1677bb;
    --ink-white: #ffffff;
    --ink-navy: #0054aa;
    --paper: #ffffff;
    --photo-sky: #7badd7;
    --photo-cloud: #e8f1f8;
  }
  * { margin: 0; padding: 0; box-sizing: border-box; }
  html, body { width: 1002px; height: 1200px; overflow: hidden; background: var(--paper); }
  .sleeve { position: relative; width: 1002px; height: 1200px; background: var(--paper); }
  .band {
    position: absolute; left: 0; width: 1002px;
    background: linear-gradient(105deg, var(--band-light) 0%, var(--band-dark) 100%);
    color: var(--ink-white);
  }
  /* Back panel, printed inverted */
  .band--back { top: 170px; height: 274px; transform: rotate(180deg); }
  .feature-title, .feature-note { position: absolute; left: 118px; white-space: nowrap; font-family: "Cousine", monospace; line-height: 1; }
  .feature-title { font-size: 23px; font-weight: 700; transform: translateY(-50%); }
  .feature-note { left: 130px; font-size: 12.5px; transform: translateY(-50%); }
  .feature-title sup { font-size: 10px; font-weight: 400; vertical-align: 4px; margin: 0 4px 0 2px; }
  .size-label { position: absolute; left: 656px; width: 224px; text-align: center; white-space: nowrap; font-family: "Montserrat", sans-serif; font-weight: 700; line-height: 1; transform: translateY(-50%); }
  .size-label--name { top: 28px; font-size: 35px; letter-spacing: 0.3px; }
  .size-label--dims { top: 78px; font-size: 33px; }
  .warranty { position: absolute; left: 565px; top: 131px; width: 188px; height: 120px; }
  .warranty svg { position: absolute; inset: 0; }
  .warranty-text { position: absolute; left: 0; width: 188px; text-align: center; white-space: nowrap; color: var(--ink-navy); font-family: "Cousine", monospace; line-height: 1; transform: translateY(-50%); }
  .warranty-text--lead { top: 56px; font-size: 13px; font-weight: 700; }
  .warranty-text--sub1 { top: 72px; font-size: 10px; }
  .warranty-text--sub2 { top: 87px; font-size: 10px; }

  /* Front panel */
  .band--front { top: 757px; height: 280px; }
  .brand-mark { position: absolute; left: 173px; top: 812px; width: 200px; display: flex; align-items: center; justify-content: center; gap: 8px; font-family: "Montserrat", sans-serif; font-weight: 600; font-size: 30px; color: var(--ink-white); }
  .brand-mark .dot { width: 12px; height: 12px; border-radius: 50%; background: var(--ink-white); }
  .product-name { position: absolute; left: 74px; width: 400px; top: 897px; text-align: center; font-family: "Montserrat", sans-serif; font-weight: 700; font-size: 42px; line-height: 53px; color: var(--ink-white); letter-spacing: 0.5px; }
  .use-note { position: absolute; left: 250px; width: 502px; top: 1009px; text-align: center; font-family: "Montserrat", sans-serif; font-weight: 600; font-size: 13px; color: var(--ink-white); }
  .hero-photo { position: absolute; left: 508px; top: 780px; width: 352px; height: 225px; border-radius: 40% 40% 30% 30%; background: radial-gradient(ellipse at 55% 80%, var(--photo-cloud) 0%, rgba(232,241,248,0.7) 40%, rgba(123,173,215,0) 75%); }
  .tagline { position: absolute; left: 768px; top: 824px; font-family: "Montserrat", sans-serif; font-weight: 800; font-size: 15px; line-height: 20px; color: var(--ink-white); letter-spacing: -0.3px; }
</style>
</head>
<body>
<div class="sleeve">

  <section class="band band--back" aria-label="Back panel">
    <p class="feature-title" style="top:39px">•Perfect For All Sleepers</p>
    <p class="feature-note" style="top:61px">Fully Adjustable for all sleeping positions</p>
    <p class="feature-title" style="top:90px">•MAPLEcomfort<sup>TM</sup>Memory Foam</p>
    <p class="feature-note" style="top:112px">Provides cloud-like comfort &amp; support</p>
    <p class="feature-title" style="top:143px">•Eco Friendly</p>
    <p class="feature-note" style="top:165px">Hypoallergenic and FoamSafe-US® certified</p>
    <p class="feature-title" style="top:194px">•Cool &amp; Anti-Bacterial</p>
    <p class="feature-note" style="top:216px">Antimicrobial, ultra-soft &amp; cool to the touch cover</p>

    <div class="warranty">
      <svg viewBox="0 0 188 120" width="188" height="120" aria-hidden="true">
        <g fill="#ffffff">
          <circle cx="90" cy="45" r="45"/>
          <circle cx="50" cy="78" r="42"/>
          <circle cx="146" cy="78" r="42"/>
          <ellipse cx="95" cy="85" rx="70" ry="35"/>
        </g>
      </svg>
      <p class="warranty-text warranty-text--lead">5-year warranty</p>
      <p class="warranty-text warranty-text--sub1">item repair or</p>
      <p class="warranty-text warranty-text--sub2">replacement</p>
    </div>

    <p class="size-label size-label--dims">20” X 30”</p>
    <p class="size-label size-label--name">QUEEN SIZE</p>
  </section>

  <section class="band band--front" aria-label="Front panel"></section>
  <div class="brand-mark"><span class="dot"></span>Maple 3</div>
  <h1 class="product-name">ADJUSTABLE<br>PILLOW</h1>
  <div class="hero-photo" role="img" aria-label="Photo of a woman hugging a pillow while sitting on a fluffy white cloud"></div>
  <p class="tagline">LIKE SLEEPING<br>ON A CLOUD</p>
  <p class="use-note">Perfect for: back, side or stomach sleepers</p>

</div>
</body>
</html>
```